High-End audio shop owner needs a business card

I need a personal Business Card for my Audio shop which exists since 1962. We offer high Quality brands, professional Attention and run our own repair-service-department. I look for a design which will be printed on high Quality paper and shall convey trust to the Client that we are very serious. Language is german.

```html
<!DOCTYPE html>
<html lang="de">
<head>
<meta charset="utf-8">
<title>Klangwerk Audio – Visitenkarte</title>
<link href="https://fonts.googleapis.com/css2?family=Roboto:wght@400;500;700;900&display=swap" rel="stylesheet">
<style>
  :root {
    --backdrop: #e4e4e6;
    --paper: #ffffff;
    --navy: #141a2b;
    --navy-deep: #0c111e;
    --orange: #f26a1b;
    --text-light: #f2f3f6;
    --text-muted: #c9ccd4;
    --divider: #5b6173;
  }
  * { box-sizing: border-box; margin: 0; padding: 0; }
  html, body {
    width: 1200px; height: 900px; overflow: hidden;
    background: var(--backdrop);
    font-family: "Roboto", Arial, sans-serif;
  }
  .canvas {
    position: relative; width: 1200px; height: 900px;
    display: flex; align-items: center; justify-content: center; gap: 40px;
  }
  .card {
    position: relative; width: 540px; height: 310px;
    border-radius: 24px; overflow: hidden;
    box-shadow: 0 14px 30px rgba(0,0,0,0.18);
  }
  .wordmark {
    font-weight: 900; color: var(--orange);
    font-size: 38px; letter-spacing: 0.5px; white-space: nowrap;
  }

  /* Front */
  .card--front { background: var(--navy); }
  .front__head {
    position: absolute; inset: 0 0 auto 0; height: 148px;
    background: var(--paper);
    display: flex; align-items: center; justify-content: center;
    padding-top: 30px;
    border-bottom: 4px solid var(--orange);
  }
  .front__body {
    position: absolute; left: 0; right: 0; top: 152px; bottom: 0;
    background: radial-gradient(ellipse at 60% 40%, var(--navy) 0%, var(--navy-deep) 100%);
    display: flex; align-items: center; padding: 0 30px 0 0;
  }
  .person {
    width: 208px; text-align: right; padding-right: 22px;
    border-right: 1px solid var(--divider);
    height: 92px; display: flex; flex-direction: column; justify-content: center;
  }
  .person__name { color: var(--orange); font-size: 17px; font-weight: 500; }
  .person__role { color: var(--text-muted); font-size: 12.5px; margin-top: 6px; }
  .contact { list-style: none; padding-left: 18px; }
  .contact__item {
    display: flex; align-items: center; gap: 10px;
    color: var(--text-light); font-size: 14px; height: 26px;
  }
  .contact__icon { width: 18px; height: 18px; flex: none; }

  /* Back */
  .card--back {
    background: radial-gradient(ellipse at 55% 45%, #1b2236 0%, var(--navy-deep) 100%);
    display: flex; align-items: center; justify-content: center;
  }
</style>
</head>
<body>
<main class="canvas">
  <section class="card card--front" aria-label="Vorderseite">
    <div class="front__head">
      <span class="wordmark">Klangwerk Audio</span>
    </div>
    <div class="front__body">
      <div class="person">
        <p class="person__name">Jonas Reiter</p>
        <p class="person__role">Manager</p>
      </div>
      <ul class="contact">
        <li class="contact__item">
          <svg class="contact__icon" viewBox="0 0 18 18"><circle cx="9" cy="9" r="9" fill="var(--orange)"/><path d="M6 4.5l2 2-1 1.2c.6 1.3 1.6 2.3 2.9 2.9l1.2-1 2 2-1.3 1.4C8.6 12.6 5.4 9.4 4.6 6z" fill="var(--navy)"/></svg>
          0851 26 73 19
        </li>
        <li class="contact__item">
          <svg class="contact__icon" viewBox="0 0 18 18"><circle cx="9" cy="9" r="9" fill="var(--orange)"/><rect x="4.5" y="5.8" width="9" height="6.4" rx="1" fill="var(--navy)"/><path d="M4.8 6.2L9 9.4l4.2-3.2" stroke="var(--orange)" stroke-width="1" fill="none"/></svg>
          info@klangwerkaudio.com
        </li>
        <li class="contact__item">
          <svg class="contact__icon" viewBox="0 0 18 18"><circle cx="9" cy="9" r="9" fill="var(--orange)"/><g stroke="var(--navy)" stroke-width="1.1" fill="none"><circle cx="9" cy="9" r="4.6"/><ellipse cx="9" cy="9" rx="2" ry="4.6"/><path d="M4.4 9h9.2"/></g></svg>
          www.klangwerkaudio.com
        </li>
        <li class="contact__item">
          <svg class="contact__icon" viewBox="0 0 18 18"><circle cx="9" cy="9" r="9" fill="var(--orange)"/><path d="M9 14s-3.6-3.8-3.6-6.3a3.6 3.6 0 017.2 0C12.6 10.2 9 14 9 14z" fill="var(--navy)"/><circle cx="9" cy="7.7" r="1.3" fill="var(--orange)"/></svg>
          No. 27410, linden road, berlin
        </li>
      </ul>
    </div>
  </section>

  <section class="card card--back" aria-label="Rückseite">
    <span class="wordmark">Klangwerk Audio</span>
  </section>
</main>
</body>
</html>
```